Harrowgate Supply Group Business Card Design

The Business Card will be one side only with Harrowgate Supplies Group Logo
Card should have:
Name
Title
Office phone Number
Cell Number
email address
Website
Street Address
Our Slogan is Solid and Dependable
Looking for something that stands out from other business cards

Target Market(s)

Heavy equipment Lease Company

```html
<!DOCTYPE html>
<html lang="en">
<head>
<meta charset="utf-8">
<title>Harrowgate Supplies Group – Business Card</title>
<link href="https://fonts.googleapis.com/css2?family=Exo+2:wght@500&family=Roboto:wght@400;700&display=swap" rel="stylesheet">
<style>
  :root {
    --page-bg: #d8d3cd;
    --card-bg: #f3f3f1;
    --brand-red: #c4262e;
    --brand-navy: #27235e;
    --text-navy: #2a2760;
    --slogan-grey: #d9d6dd;
  }
  html, body {
    margin: 0;
    width: 1200px;
    height: 1054px;
    overflow: hidden;
    background: var(--page-bg);
  }
  .card {
    position: absolute;
    left: 100px;
    top: 225px;
    width: 1000px;
    height: 603px;
    background: var(--card-bg);
    box-shadow: 0 18px 40px rgba(0,0,0,0.18);
    overflow: hidden;
    font-family: "Roboto", Arial, sans-serif;
    color: var(--text-navy);
  }
  .wordmark {
    position: absolute;
    left: 40px;
    width: 494px;
    top: 262px;
    text-align: center;
    font-family: "Roboto", Arial, sans-serif;
    font-weight: 700;
    color: var(--brand-red);
    font-size: 40px;
    line-height: 1.15;
    letter-spacing: 0.5px;
  }
  .wordmark-square {
    display: block;
    width: 34px;
    height: 34px;
    margin: 0 auto 22px;
    background: var(--brand-red);
  }
  .contact {
    position: absolute;
    left: 590px;
    top: 105px;
  }
  .person-name {
    margin: 0;
    font-family: "Exo 2", "Roboto", sans-serif;
    font-weight: 500;
    font-size: 40px;
    color: var(--brand-red);
    line-height: 1.1;
  }
  .person-title {
    margin: 8px 0 42px;
    font-size: 24px;
    color: var(--text-navy);
  }
  .contact-list {
    list-style: none;
    margin: 0;
    padding: 0;
  }
  .contact-list li {
    display: flex;
    align-items: center;
    height: 35.5px;
    font-size: 24px;
  }
  .contact-list svg {
    width: 20px;
    height: 20px;
    margin: 0 24px 0 8px;
    fill: var(--brand-red);
    flex: none;
  }
  .address {
    margin: 8px 0 0;
    font-size: 24px;
    line-height: 35px;
  }
  .bands {
    position: absolute;
    left: 0;
    bottom: 0;
    width: 1000px;
    height: 76px;
  }
  .slogan {
    position: absolute;
    left: 590px;
    bottom: 22px;
    margin: 0;
    font-size: 24px;
    color: var(--slogan-grey);
  }
</style>
</head>
<body>
  <div class="card">
    <div class="wordmark">
      <span class="wordmark-square"></span>
      HARROWGATE SUPPLIES<br>GROUP
    </div>

    <div class="contact">
      <h1 class="person-name">Daniel Harrow</h1>
      <p class="person-title">Managing Director</p>
      <ul class="contact-list">
        <li>
          <svg viewBox="0 0 24 24" aria-hidden="true"><path d="M3 9c0-3 4-5 9-5s9 2 9 5v2h-5V9c-1-.6-2.5-1-4-1s-3 .4-4 1v2H3V9zm3 4h12l2 7H4l2-7zm6 1.5a2.5 2.5 0 100 5 2.5 2.5 0 000-5z"/></svg>
          555-210-7788
        </li>
        <li>
          <svg viewBox="0 0 24 24" aria-hidden="true"><path d="M6 2h12v6H6zM3 9h18a1 1 0 011 1v7h-4v5H6v-5H2v-7a1 1 0 011-1zm5 7v4h8v-4z"/></svg>
          555-210-7799
        </li>
        <li>
          <svg viewBox="0 0 24 24" aria-hidden="true"><path d="M2 5h20v14H2zm2 2v1l8 5 8-5V7l-8 5z"/></svg>
          name@harrowgatesupply.com
        </li>
        <li>
          <svg viewBox="0 0 24 24" aria-hidden="true"><path d="M12 2a10 10 0 100 20 10 10 0 000-20zm-1 2.1V8H7.6A8 8 0 0111 4.1zm2 0A8 8 0 0116.4 8H13zM5 10h6v4H5a8 8 0 010-4zm8 0h6a8 8 0 010 4h-6zm-5.4 6H11v3.9A8 8 0 017.6 16zM13 16h3.4a8 8 0 01-3.4 3.9z"/></svg>
          www.harrowgatesupply.com
        </li>
      </ul>
      <p class="address">48 Quarry Road, Millbrook,<br>Stonefield, Country 40217</p>
    </div>

    <svg class="bands" viewBox="0 0 1000 76" aria-hidden="true">
      <rect x="0" y="53" width="700" height="23" fill="var(--brand-red)"/>
      <path d="M462 76 C505 40 520 0 580 0 H1000 V76 Z" fill="var(--brand-navy)"/>
    </svg>
    <p class="slogan">Solid and Dependable</p>
  </div>
</body>
</html>
```